Unusual Options Activity Graphic Card Design for Finance App

We are developing a financial data platform called Vantix Pulse, and we need a visually striking, mobile-optimized graphic card design to display unusual options activity. The card will be featured in our mobile app and marketing materials, inspired by platforms like Marlocq and Pindrake Lane.
🔹 Design Goals:
Modern, clean, and professional aesthetic
Use vibrant electric blue, green, or dark theme gradients
Must feel tech-savvy and finance-oriented
Layout should be optimized for vertical mobile format (portrait)
🔹 Information to Include in the Card:
Ticker Symbol (e.g., QZR) with colored badge
Date & Time of trade
Trade Type (e.g., Sweep Call / Put)
Execution Type (At Ask or At Bid)
Strike Price
Expiration Date
Premium (e.g., $342.75K)
Size@Price (e.g., 6995@$0.49)
Volume
Open Interest
Branding at bottom: “Vantix Pulse” in modern font
🔹 Inspiration:
Marlocq’s profit/loss cards
Clean fintech dashboards (Quillmere, Pindrake Lane, Haskvorn Console)
Please provide the final deliverable in high-resolution PNG and layered PSD or Figma file for future edits.
Stock Market Traders
Finance

```html
<!DOCTYPE html>
<html lang="en">
<head>
<meta charset="utf-8">
<title>Unusual Options Activity – Card Design for Vantix Pulse</title>
<link href="https://fonts.googleapis.com/css2?family=Inter:wght@400;500;600;700;800&family=Roboto:wght@400;500;700;900&display=swap" rel="stylesheet">
<style>
  :root{
    --bg:#000;
    --ink:#fff;
    --muted:#a9b3cc;
    --green:#4cc35a;
    --red:#e0413e;
    --navy-1:#0b1633;
    --navy-2:#142a66;
    --panel:#1a1a1a;
    --field:#2c2c2e;
    --bar:#4a4a4c;
  }
  *{box-sizing:border-box;margin:0;padding:0}
  html,body{width:1200px;height:975px;overflow:hidden;background:var(--bg)}
  body{position:relative;font-family:'Inter',sans-serif;color:var(--ink)}
  .abs{position:absolute}

  /* Heading */
  .board-title{left:40px;top:33px;width:320px;text-align:center;font:800 21px/1.17 'Inter',sans-serif;letter-spacing:-0.3px}

  /* Annotations */
  .note{font:700 13.5px/1 'Inter',sans-serif;white-space:nowrap}
  .note--right{text-align:right}
  .annotations{left:0;top:0;width:1200px;height:975px;pointer-events:none}

  /* Card */
  .card{position:absolute;width:129px;height:215px;border-radius:4px;overflow:hidden;font-family:'Roboto',sans-serif;
    background:
      radial-gradient(70% 45% at 20% 85%, rgba(40,140,70,.35), transparent 70%),
      radial-gradient(60% 50% at 75% 40%, rgba(60,120,90,.22), transparent 70%),
      linear-gradient(170deg,var(--navy-1) 0%,#10235a 55%,var(--navy-2) 100%);}
  .card__title{position:absolute;left:12px;top:12px;font:700 22.5px/1 'Roboto',sans-serif;letter-spacing:.2px}
  .card__subtitle{position:absolute;left:12px;top:37px;font:500 11px/1 'Roboto',sans-serif;letter-spacing:.1px}
  .card__meta{position:absolute;left:12px;top:52px;display:flex;height:12px;border:1px solid #c9ccd6;border-radius:1.5px;width:106px}
  .card__ticker{background:var(--green);color:#0b1633;font:700 7px/10px 'Roboto',sans-serif;padding:0 4px;width:23px;text-align:center}
  .card__ticker--red{background:var(--red);color:#fff}
  .card__stamp{flex:1;text-align:center;font:400 7.5px/10px 'Roboto',sans-serif}
  .card__trade{position:absolute;left:12px;top:73px;font:700 17.5px/1 'Roboto',sans-serif;letter-spacing:.3px;white-space:nowrap}
  .is-green{color:var(--green)}
  .is-red{color:var(--red)}
  .card__exec{position:absolute;left:12px;top:94px;font:400 8.5px/1 'Roboto',sans-serif}
  .card__stats{position:absolute;left:12px;top:112px;display:grid;grid-template-columns:53px 60px;row-gap:7px}
  .stat__label{font:400 5.5px/1 'Roboto',sans-serif;color:var(--muted);letter-spacing:.2px}
  .stat__value{font:700 8px/1 'Roboto',sans-serif;margin-top:4px}
  .card__footer{position:absolute;left:8px;right:8px;top:187px;height:16px}
  .avatar{position:absolute;left:0;top:0;width:15px;height:15px;border-radius:50%;background:radial-gradient(circle at 40% 40%,#e8e8ee,#8b8f9c)}
  .card__user{position:absolute;left:20px;top:1px;font:700 5.5px/1 'Roboto',sans-serif}
  .card__posted{position:absolute;left:20px;top:9px;font:400 4.5px/1 'Roboto',sans-serif;color:var(--muted)}
  .brand{position:absolute;right:0;top:5px;display:flex;align-items:center;gap:2px;font:700 5px/1 'Roboto',sans-serif;color:var(--green)}
  .brand__dot{width:5px;height:5px;border-radius:50%;background:var(--green)}

  /* Section labels */
  .section-label{font:700 17px/1 'Inter',sans-serif}

  /* Mobile app */
  .app{left:100px;top:590px;width:170px;height:355px;overflow:hidden}
  .app__status{position:absolute;left:21px;top:5px;font:600 6.5px/1 'Inter',sans-serif}
  .app__sys{position:absolute;right:18px;top:5px;display:flex;gap:3px;align-items:center}
  .app__heading{position:absolute;left:0;width:170px;top:22px;text-align:center;font:500 8px/1 'Inter',sans-serif}
  .app__tabs{position:absolute;left:6px;right:6px;top:36px;display:flex;justify-content:space-around;font:500 5.5px/1 'Inter',sans-serif;border-bottom:1px solid #262626;padding-bottom:5px}
  .app__tab--active{color:var(--green)}
  .app__viewport{position:absolute;left:0;top:50px;width:170px;height:266px;overflow:hidden}
  .app__nav{position:absolute;left:0;top:320px;width:170px;display:flex;justify-content:space-around;align-items:flex-end;font:500 5px/1 'Inter',sans-serif;color:#bbb}
  .app__nav-item{display:flex;flex-direction:column;align-items:center;gap:2px}
  .app__nav-item--active{color:var(--green)}
  .home-bar{position:absolute;height:2px;border-radius:1px;background:#ddd}

  /* Web app */
  .web{left:290px;top:583px;width:166px;height:358px;border-radius:7px;overflow:hidden;background:#000}
  .web__status{position:absolute;left:0;top:0;width:166px;height:24px;background:#fff;color:#000}
  .web__status-time{position:absolute;left:19px;top:9px;font:600 6.5px/1 'Inter',sans-serif}
  .web__header{position:absolute;left:0;top:24px;width:166px;height:35px;background:#111}
  .web__logo{position:absolute;left:4px;top:12px;width:11px;height:11px;border-radius:50%;background:var(--green)}
  .web__app-name{position:absolute;left:23px;top:15px;font:600 5.5px/1 'Inter',sans-serif}
  .toggle{position:absolute;border-radius:6px;background:#fff}
  .toggle__knob{position:absolute;border-radius:50%;background:#111}
  .web__panel{position:absolute;left:0;top:59px;width:166px;height:78px;background:var(--panel)}
  .web__panel-title{position:absolute;left:4px;top:7px;font:500 7.5px/1 'Inter',sans-serif}
  .web__auto{position:absolute;left:22px;top:26px;font:400 5.2px/1 'Inter',sans-serif}
  .web__search{position:absolute;left:4px;top:43px;width:156px;height:15px;border-radius:2px;background:var(--field);font:400 5.3px/15px 'Inter',sans-serif;color:#aaa;padding-left:6px}
  .web__tools{position:absolute;left:12px;top:66px;display:flex;gap:8px;font:400 5px/1 'Inter',sans-serif}
  .web__tool{display:flex;align-items:center;gap:3px}
  .web__viewport{position:absolute;left:0;top:137px;width:166px;height:172px;overflow:hidden}
  .web__browser{position:absolute;left:0;top:309px;width:166px;height:49px;background:var(--bar)}
  .web__url{position:absolute;left:13px;top:2px;width:140px;height:15px;border-radius:4px;background:#3a3a3c;font:400 5.8px/15px 'Inter',sans-serif;text-align:center;color:#eee}
  .web__browser-icons{position:absolute;left:8px;right:8px;top:22px;display:flex;justify-content:space-between}

  /* Closing */
  .thanks{left:850px;top:845px;width:350px;text-align:center}
  .thanks__title{font:800 45px/1 'Inter',sans-serif;letter-spacing:-2.2px}
  .thanks__text{margin-top:10px;font:400 16px/1.25 'Inter',sans-serif}
</style>
</head>
<body>

<h1 class="abs board-title">Unusual Options Activity :<br>Graphic Card Design for<br>Finance App</h1>

<!-- Annotated card -->
<div class="note abs note--right" style="left:87px;top:259px">Ticker Symbol</div>
<div class="note abs note--right" style="left:107px;top:281px">Trade Type</div>
<div class="note abs note--right" style="left:80px;top:299px">Execution Type</div>
<div class="note abs note--right" style="left:117px;top:401px">Branding</div>
<div class="note abs" style="left:385px;top:242px">Date &amp; Time of trade</div>
<div class="note abs" style="left:413px;top:277px">C/P</div>

<svg class="abs annotations" viewBox="0 0 1200 975" aria-hidden="true">
  <g fill="none" stroke="#fff" stroke-width="1.2" stroke-linecap="round">
    <path d="M186 265 C195 250 220 250 230 260"/><path d="M226 257 L231 261 L225 262"/>
    <path d="M186 288 C200 281 218 281 232 285"/><path d="M227 282 L233 285 L227 288"/>
    <path d="M186 306 C200 299 218 299 232 301"/><path d="M227 298 L233 301 L227 304"/>
    <path d="M186 408 C198 394 218 394 230 406"/><path d="M225 405 L231 407 L228 401"/>
    <path d="M384 249 C375 238 358 240 351 254"/><path d="M349 248 L350 255 L356 252"/>
    <path d="M407 284 C395 272 368 276 352 285"/><path d="M357 281 L351 285 L357 288"/>
  </g>
  <g fill="#fff">
    <circle cx="186" cy="265" r="2"/><circle cx="186" cy="288" r="2"/><circle cx="186" cy="306" r="2"/>
    <circle cx="186" cy="408" r="2"/><circle cx="385" cy="249" r="2"/><circle cx="408" cy="284" r="2"/>
  </g>
</svg>

<div class="card" style="left:229px;top:205px">
  <div class="card__title">UNUSUAL</div><div class="card__subtitle">OPTIONS ACTIVITY</div>
  <div class="card__meta"><span class="card__ticker">KVD</span><span class="card__stamp">04/05/25 | 10:32:12</span></div>
  <div class="card__trade">TRADE <span class="is-green">CALL</span></div>
  <div class="card__exec is-green">AT ASk</div>
  <div class="card__stats">
    <div><div class="stat__label">STRIKE</div><div class="stat__value">$91</div></div>
    <div><div class="stat__label">EXPIRATION</div><div class="stat__value">19 Apr 25</div></div>
    <div><div class="stat__label">PREMIUM</div><div class="stat__value">$342.75K</div></div>
    <div><div class="stat__label">SIZE@PRICE</div><div class="stat__value">6995@$0.49</div></div>
    <div><div class="stat__label">VOLUME</div><div class="stat__value">34.7K</div></div>
    <div><div class="stat__label">OPEN INTEREST</div><div class="stat__value">2424</div></div>
  </div>
  <div class="card__footer"><div class="avatar" role="img" aria-label="User avatar photo"></div><div class="card__user">Nuvra</div><div class="card__posted">04/07/2025 · 3:34 PM EST</div><div class="brand"><span class="brand__dot"></span>Vantix Pulse</div></div>
</div>

<!-- Variations grid -->
<div class="card" style="left:585px;top:228px">
  <div class="card__title">UNUSUAL</div><div class="card__subtitle">OPTIONS ACTIVITY</div>
  <div class="card__meta"><span class="card__ticker">KVD</span><span class="card__stamp">04/05/25 | 10:32:12</span></div>
  <div class="card__trade">SWEEP <span class="is-red">PUT</span></div>
  <div class="card__exec is-green">AT ASK</div>
  <div class="card__stats">
    <div><div class="stat__label">STRIKE</div><div class="stat__value">$91</div></div>
    <div><div class="stat__label">EXPIRATION</div><div class="stat__value">19 Apr 25</div></div>
    <div><div class="stat__label">PREMIUM</div><div class="stat__value">$342.75K</div></div>
    <div><div class="stat__label">SIZE@PRICE</div><div class="stat__value">6995@$0.49</div></div>
    <div><div class="stat__label">VOLUME</div><div class="stat__value">34.7K</div></div>
    <div><div class="stat__label">OPEN INTEREST</div><div class="stat__value">2424</div></div>
  </div>
  <div class="card__footer"><div class="avatar" role="img" aria-label="User avatar photo"></div><div class="card__user">Nuvra</div><div class="card__posted">04/07/2025 · 3:34 PM EST</div><div class="brand"><span class="brand__dot"></span>Vantix Pulse</div></div>
</div>

<div class="card" style="left:719px;top:228px">
  <div class="card__title">UNUSUAL</div><div class="card__subtitle">OPTIONS ACTIVITY</div>
  <div class="card__meta"><span class="card__ticker">KVD</span><span class="card__stamp">04/05/25 | 10:32:12</span></div>
  <div class="card__trade">TRADE <span class="is-green">CALL</span></div>
  <div class="card__exec is-red">AT BID</div>
  <div class="card__stats">
    <div><div class="stat__label">STRIKE</div><div class="stat__value">$91</div></div>
    <div><div class="stat__label">EXPIRATION</div><div class="stat__value">19 Apr 25</div></div>
    <div><div class="stat__label">PREMIUM</div><div class="stat__value">$342.75K</div></div>
    <div><div class="stat__label">SIZE@PRICE</div><div class="stat__value">6995@$0.49</div></div>
    <div><div class="stat__label">VOLUME</div><div class="stat__value">34.7K</div></div>
    <div><div class="stat__label">OPEN INTEREST</div><div class="stat__value">2424</div></div>
  </div>
  <div class="card__footer"><div class="avatar" role="img" aria-label="User avatar photo"></div><div class="card__user">Nuvra</div><div class="card__posted">04/07/2025 · 3:34 PM EST</div><div class="brand"><span class="brand__dot"></span>Vantix Pulse</div></div>
</div>

<div class="card" style="left:853px;top:228px">
  <div class="card__title">UNUSUAL</div><div class="card__subtitle">OPTIONS ACTIVITY</div>
  <div class="card__meta"><span class="card__ticker">KVD</span><span class="card__stamp">04/05/25 | 10:32:12</span></div>
  <div class="card__trade">TRADE <span class="is-green">CALL</span></div>
  <div class="card__exec is-green">AT ASK</div>
  <div class="card__stats">
    <div><div class="stat__label">STRIKE</div><div class="stat__value">$91</div></div>
    <div><div class="stat__label">EXPIRATION</div><div class="stat__value">19 Apr 25</div></div>
    <div><div class="stat__label">PREMIUM</div><div class="stat__value">$342.75K</div></div>
    <div><div class="stat__label">SIZE@PRICE</div><div class="stat__value">6995@$0.49</div></div>
    <div><div class="stat__label">VOLUME</div><div class="stat__value">34.7K</div></div>
    <div><div class="stat__label">OPEN INTEREST</div><div class="stat__value">2424</div></div>
  </div>
  <div class="card__footer"><div class="avatar" role="img" aria-label="User avatar photo"></div><div class="card__user">Nuvra</div><div class="card__posted">04/07/2025 · 3:34 PM EST</div><div class="brand"><span class="brand__dot"></span>Vantix Pulse</div></div>
</div>

<div class="card" style="left:987px;top:228px">
  <div class="card__title">UNUSUAL</div><div class="card__subtitle">OPTIONS ACTIVITY</div>
  <div class="card__meta"><span class="card__ticker">KVD</span><span class="card__stamp">04/05/25 | 10:32:12</span></div>
  <div class="card__trade">TRADE <span class="is-red">PUT</span></div>
  <div class="card__exec is-red">AT BID</div>
  <div class="card__stats">
    <div><div class="stat__label">STRIKE</div><div class="stat__value">$91</div></div>
    <div><div class="stat__label">EXPIRATION</div><div class="stat__value">19 Apr 25</div></div>
    <div><div class="stat__label">PREMIUM</div><div class="stat__value">$342.75K</div></div>
    <div><div class="stat__label">SIZE@PRICE</div><div class="stat__value">6995@$0.49</div></div>
    <div><div class="stat__label">VOLUME</div><div class="stat__value">34.7K</div></div>
    <div><div class="stat__label">OPEN INTEREST</div><div class="stat__value">2424</div></div>
  </div>
  <div class="card__footer"><div class="avatar" role="img" aria-label="User avatar photo"></div><div class="card__user">Nuvra</div><div class="card__posted">04/07/2025 · 3:34 PM EST</div><div class="brand"><span class="brand__dot"></span>Vantix Pulse</div></div>
</div>

<div class="card" style="left:585px;top:460px">
  <div class="card__title">UNUSUAL</div><div class="card__subtitle">OPTIONS ACTIVITY</div>
  <div class="card__meta"><span class="card__ticker card__ticker--red">KVD</span><span class="card__stamp">04/05/25 | 10:32:12</span></div>
  <div class="card__trade">SWEEP <span class="is-red">PUT</span></div>
  <div class="card__exec is-green">AT ASK</div>
  <div class="card__stats">
    <div><div class="stat__label">STRIKE</div><div class="stat__value">$91</div></div>
    <div><div class="stat__label">EXPIRATION</div><div class="stat__value">19 Apr 25</div></div>
    <div><div class="stat__label">PREMIUM</div><div class="stat__value">$342.75K</div></div>
    <div><div class="stat__label">SIZE@PRICE</div><div class="stat__value">6995@$0.49</div></div>
    <div><div class="stat__label">VOLUME</div><div class="stat__value">34.7K</div></div>
    <div><div class="stat__label">OPEN INTEREST</div><div class="stat__value">2424</div></div>
  </div>
  <div class="card__footer"><div class="avatar" role="img" aria-label="User avatar photo"></div><div class="card__user">Nuvra</div><div class="card__posted">04/07/2025 · 3:34 PM EST</div><div class="brand"><span class="brand__dot"></span>Vantix Pulse</div></div>
</div>

<div class="card" style="left:719px;top:460px">
  <div class="card__title">UNUSUAL</div><div class="card__subtitle">OPTIONS ACTIVITY</div>
  <div class="card__meta"><span class="card__ticker card__ticker--red">KVD</span><span class="card__stamp">04/05/25 | 10:32:12</span></div>
  <div class="card__trade">SWEEP <span class="is-green">CALL</span></div>
  <div class="card__exec is-red">AT BID</div>
  <div class="card__stats">
    <div><div class="stat__label">STRIKE</div><div class="stat__value">$91</div></div>
    <div><div class="stat__label">EXPIRATION</div><div class="stat__value">19 Apr 25</div></div>
    <div><div class="stat__label">PREMIUM</div><div class="stat__value">$342.75K</div></div>
    <div><div class="stat__label">SIZE@PRICE</div><div class="stat__value">6995@$0.49</div></div>
    <div><div class="stat__label">VOLUME</div><div class="stat__value">34.7K</div></div>
    <div><div class="stat__label">OPEN INTEREST</div><div class="stat__value">2424</div></div>
  </div>
  <div class="card__footer"><div class="avatar" role="img" aria-label="User avatar photo"></div><div class="card__user">Nuvra</div><div class="card__posted">04/07/2025 · 3:34 PM EST</div><div class="brand"><span class="brand__dot"></span>Vantix Pulse</div></div>
</div>

<div class="card" style="left:853px;top:460px">
  <div class="card__title">UNUSUAL</div><div class="card__subtitle">OPTIONS ACTIVITY</div>
  <div class="card__meta"><span class="card__ticker card__ticker--red">KVD</span><span class="card__stamp">04/05/25 | 10:32:12</span></div>
  <div class="card__trade">TRADE <span class="is-green">CALL</span></div>
  <div class="card__exec is-green">AT ASk</div>
  <div class="card__stats">
    <div><div class="stat__label">STRIKE</div><div class="stat__value">$91</div></div>
    <div><div class="stat__label">EXPIRATION</div><div class="stat__value">19 Apr 25</div></div>
    <div><div class="stat__label">PREMIUM</div><div class="stat__value">$342.75K</div></div>
    <div><div class="stat__label">SIZE@PRICE</div><div class="stat__value">6995@$0.49</div></div>
    <div><div class="stat__label">VOLUME</div><div class="stat__value">34.7K</div></div>
    <div><div class="stat__label">OPEN INTEREST</div><div class="stat__value">2424</div></div>
  </div>
  <div class="card__footer"><div class="avatar" role="img" aria-label="User avatar photo"></div><div class="card__user">Nuvra</div><div class="card__posted">04/07/2025 · 3:34 PM EST</div><div class="brand"><span class="brand__dot"></span>Vantix Pulse</div></div>
</div>

<div class="card" style="left:987px;top:460px">
  <div class="card__title">UNUSUAL</div><div class="card__subtitle">OPTIONS ACTIVITY</div>
  <div class="card__meta"><span class="card__ticker card__ticker--red">KVD</span><span class="card__stamp">04/05/25 | 10:32:12</span></div>
  <div class="card__trade">TRADE <span class="is-red">PUT</span></div>
  <div class="card__exec is-red">AT ASk</div>
  <div class="card__stats">
    <div><div class="stat__label">STRIKE</div><div class="stat__value">$91</div></div>
    <div><div class="stat__label">EXPIRATION</div><div class="stat__value">19 Apr 25</div></div>
    <div><div class="stat__label">PREMIUM</div><div class="stat__value">$342.75K</div></div>
    <div><div class="stat__label">SIZE@PRICE</div><div class="stat__value">6995@$0.49</div></div>
    <div><div class="stat__label">VOLUME</div><div class="stat__value">34.7K</div></div>
    <div><div class="stat__label">OPEN INTEREST</div><div class="stat__value">2424</div></div>
  </div>
  <div class="card__footer"><div class="avatar" role="img" aria-label="User avatar photo"></div><div class="card__user">Nuvra</div><div class="card__posted">04/07/2025 · 3:34 PM EST</div><div class="brand"><span class="brand__dot"></span>Vantix Pulse</div></div>
</div>

<!-- Section labels -->
<div class="abs section-label" style="left:158px;top:549px">APP</div>
<div class="abs section-label" style="left:334px;top:545px">Web APP</div>

<!-- Mobile app screen -->
<div class="abs app">
  <div class="app__status">7:09 ▴</div>
  <div class="app__sys">
    <svg width="9" height="6" viewBox="0 0 9 6" aria-hidden="true"><g fill="#fff"><rect x="0" y="4" width="1.5" height="2"/><rect x="2.5" y="3" width="1.5" height="3"/><rect x="5" y="1.5" width="1.5" height="4.5"/><rect x="7.5" y="0" width="1.5" height="6"/></g></svg>
    <svg width="8" height="6" viewBox="0 0 8 6" aria-hidden="true"><path d="M0 2 Q4 -1 8 2 L4 6 Z" fill="#fff"/></svg>
    <svg width="12" height="6" viewBox="0 0 12 6" aria-hidden="true"><rect x=".5" y=".5" width="10" height="5" rx="1.2" fill="none" stroke="#fff"/><rect x="1.5" y="1.5" width="8" height="3" fill="#fff"/></svg>
  </div>
  <div class="app__heading">Markets</div>
  <div class="app__tabs">
    <span class="app__tab--active">Option Flow</span><span>Darkpool</span><span>Treemap</span><span>Gamma</span><span>Snaps</span>
  </div>
  <div class="app__viewport">
    <div class="card" style="left:19px;top:10px">
      <div class="card__title">UNUSUAL</div><div class="card__subtitle">OPTIONS ACTIVITY</div>
      <div class="card__meta"><span class="card__ticker">KVD</span><span class="card__stamp">04/05/25 | 10:32:12</span></div>
      <div class="card__trade">TRADE <span class="is-green">CALL</span></div>
      <div class="card__exec is-green">AT ASK</div>
      <div class="card__stats">
        <div><div class="stat__label">STRIKE</div><div class="stat__value">$91</div></div>
        <div><div class="stat__label">EXPIRATION</div><div class="stat__value">19 Apr 25</div></div>
        <div><div class="stat__label">PREMIUM</div><div class="stat__value">$342.75K</div></div>
        <div><div class="stat__label">SIZE@PRICE</div><div class="stat__value">6995@$0.49</div></div>
        <div><div class="stat__label">VOLUME</div><div class="stat__value">34.7K</div></div>
        <div><div class="stat__label">OPEN INTEREST</div><div class="stat__value">2424</div></div>
      </div>
      <div class="card__footer"><div class="avatar" role="img" aria-label="User avatar photo"></div><div class="card__user">Nuvra</div><div class="card__posted">04/07/2025 · 3:34 PM EST</div><div class="brand"><span class="brand__dot"></span>Vantix Pulse</div></div>
    </div>
    <div class="card" style="left:19px;top:231px">
      <div class="card__title">UNUSUAL</div><div class="card__subtitle">OPTIONS ACTIVITY</div>
    </div>
  </div>
  <div class="app__nav">
    <span class="app__nav-item"><svg width="7" height="7" viewBox="0 0 7 7" aria-hidden="true"><g fill="#bbb"><rect width="3" height="3"/><rect x="4" width="3" height="3"/><rect y="4" width="3" height="3"/><rect x="4" y="4" width="3" height="3"/></g></svg></span>
    <span class="app__nav-item"><svg width="6" height="7" viewBox="0 0 6 7" aria-hidden="true"><rect width="6" height="7" rx="1" fill="#bbb"/><path d="M1 2.5h4M1 4.5h4" stroke="#000" stroke-width=".7"/></svg></span>
    <span class="app__nav-item app__nav-item--active"><svg width="8" height="6" viewBox="0 0 8 6" aria-hidden="true"><path d="M0 5 L3 2 L5 4 L8 1" fill="none" stroke="#4cc35a" stroke-width="1"/></svg>Markets</span>
    <span class="app__nav-item"><svg width="7" height="7" viewBox="0 0 7 7" aria-hidden="true"><g fill="#bbb"><rect y="3" width="1.6" height="4"/><rect x="2.7" y="0" width="1.6" height="7"/><rect x="5.4" y="2" width="1.6" height="5"/></g></svg></span>
    <span class="app__nav-item"><svg width="6" height="7" viewBox="0 0 6 7" aria-hidden="true"><circle cx="3" cy="2" r="1.7" fill="#bbb"/><path d="M0 7 Q3 2.5 6 7Z" fill="#bbb"/></svg></span>
  </div>
  <div class="home-bar" style="left:53px;top:347px;width:59px"></div>
</div>

<!-- Web app screen -->
<div class="abs web">
  <div class="web__status">
    <div class="web__status-time">7:09 ▴</div>
    <svg class="abs" style="right:16px;top:9px" width="32" height="6" viewBox="0 0 32 6" aria-hidden="true">
      <g fill="#000"><rect x="0" y="4" width="1.5" height="2"/><rect x="2.5" y="3" width="1.5" height="3"/><rect x="5" y="1.5" width="1.5" height="4.5"/><rect x="7.5" y="0" width="1.5" height="6"/><path d="M11 2 Q15 -1 19 2 L15 6Z"/><rect x="21.5" y=".5" width="10" height="5" rx="1.2" fill="none" stroke="#000"/><rect x="22.5" y="1.5" width="8" height="3"/></g>
    </svg>
  </div>
  <div class="web__header">
    <div class="web__logo"></div>
    <div class="web__app-name">Option Flow</div>
    <div class="toggle" style="left:91px;top:12px;width:22px;height:11px"><div class="toggle__knob" style="left:2px;top:1.5px;width:8px;height:8px"></div></div>
    <div class="avatar" role="img" aria-label="User avatar photo" style="left:119px;top:12px;width:12px;height:12px"></div>
    <svg class="abs" style="left:137px;top:16px" width="5" height="3" viewBox="0 0 5 3" aria-hidden="true"><path d="M0 0 L2.5 3 L5 0" fill="none" stroke="#bbb" stroke-width=".8"/></svg>
    <svg class="abs" style="left:151px;top:14px" width="6" height="5" viewBox="0 0 6 5" aria-hidden="true"><path d="M0 .5h6M0 2.5h6M0 4.5h6" stroke="#ddd" stroke-width=".8"/></svg>
  </div>
  <div class="web__panel">
    <div class="web__panel-title">Option Flow Data</div>
    <div class="toggle" style="left:5px;top:26px;width:12px;height:6px"><div class="toggle__knob" style="left:1px;top:1px;width:4px;height:4px"></div></div>
    <div class="web__auto">Auto Refresh</div>
    <div class="web__search">Search Ticker...</div>
    <div class="web__tools">
      <span class="web__tool"><svg width="7" height="5" viewBox="0 0 7 5" aria-hidden="true"><path d="M0 .5h7M1.5 2.5h4M2.8 4.5h1.4" stroke="#fff" stroke-width=".8"/></svg>Filter</span>
      <span class="web__tool"><svg width="6" height="7" viewBox="0 0 6 7" aria-hidden="true"><path d="M3 0v4.5M1.5 1.5L3 0l1.5 1.5M1 3H.5v3.5h5V3H5" fill="none" stroke="#fff" stroke-width=".7"/></svg>Export</span>
    </div>
  </div>
  <div class="web__viewport">
    <div class="card" style="left:18px;top:18px">
      <div class="card__title">UNUSUAL</div><div class="card__subtitle">OPTIONS ACTIVITY</div>
      <div class="card__meta"><span class="card__ticker">KVD</span><span class="card__stamp">04/05/25 | 10:32:12</span></div>
      <div class="card__trade">TRADE <span class="is-green">CALL</span></div>
      <div class="card__exec is-green">AT ASk</div>
      <div class="card__stats">
        <div><div class="stat__label">STRIKE</div><div class="stat__value">$91</div></div>
        <div><div class="stat__label">EXPIRATION</div><div class="stat__value">19 Apr 25</div></div>
        <div><div class="stat__label">PREMIUM</div><div class="stat__value">$342.75K</div></div>
        <div><div class="stat__label">SIZE@PRICE</div><div class="stat__value">6995@$0.49</div></div>
      </div>
    </div>
  </div>
  <div class="web__browser">
    <div class="web__url">🔒 app.vantixpulse.com</div>
    <div class="web__browser-icons">
      <svg width="6" height="8" viewBox="0 0 6 8" aria-hidden="true"><path d="M5 0L1 4l4 4" fill="none" stroke="#4e8cf5" stroke-width="1"/></svg>
      <svg width="6" height="8" viewBox="0 0 6 8" aria-hidden="true"><path d="M1 0l4 4-4 4" fill="none" stroke="#777" stroke-width="1"/></svg>
      <svg width="8" height="9" viewBox="0 0 8 9" aria-hidden="true"><path d="M4 0v5.5M2 2L4 0l2 2M2 4H.5v4.5h7V4H6" fill="none" stroke="#4e8cf5" stroke-width=".8"/></svg>
      <svg width="10" height="8" viewBox="0 0 10 8" aria-hidden="true"><path d="M5 1.5Q2.5 0 .5 1v6.5Q2.5 6.5 5 8Q7.5 6.5 9.5 7.5V1Q7.5 0 5 1.5v6.5" fill="none" stroke="#4e8cf5" stroke-width=".8"/></svg>
      <svg width="8" height="8" viewBox="0 0 8 8" aria-hidden="true"><rect x="2" y=".5" width="5.5" height="5.5" rx="1" fill="none" stroke="#4e8cf5" stroke-width=".8"/><rect x=".5" y="2" width="5.5" height="5.5" rx="1" fill="#4a4a4c" stroke="#4e8cf5" stroke-width=".8"/></svg>
    </div>
    <div class="home-bar" style="left:54px;top:45px;width:58px"></div>
  </div>
</div>

<!-- Closing -->
<div class="abs thanks">
  <div class="thanks__title">Thank you</div>
  <p class="thanks__text">Your feedback matters to us. Let us<br>know what you think!</p>
</div>

</body>
</html>
```